Newsletter-Design für eine Yogalehrerin
Zielgruppe
Ich bin Yogalehrerin.
Meine Zielgruppe sind hauptsächlich Erwachsene (Frauen und Männer) welche Privatyoga Online praktizieren.
Aufgabenstellung
Gerne auch, aber nicht nur das Layout und die Texte von der Webseite www.atemkreis-nord.ch verwenden.
Es sollte ein ansprechender Newsletter für Online Privatyoga gestaltet werden um mehr Teilnehmer zu gewinnen.

```html
<!DOCTYPE html>
<html lang="de">
<head>
<meta charset="utf-8">
<title>Atemkreis Nord – Newsletter Online Privatyoga</title>
<link href="https://fonts.googleapis.com/css2?family=Yanone+Kaffeesatz:wght@300;400&family=Open+Sans:wght@300;400;600;700&family=Kaushan+Script&display=swap" rel="stylesheet">
<style>
  :root{
    --page:#ffffff;
    --sand:#ede4dc;
    --card:#f4efe8;
    --accent:#ea5b35;
    --ink:#4a4a4a;
    --muted:#8a8580;
    --adult:#9b8cc9;
    --kids:#f19a8b;
    --mama:#7cc5e3;
    --senior:#5aa39a;
  }
  *{box-sizing:border-box;margin:0;padding:0}
  html,body{width:741px;height:1200px;overflow:hidden;background:var(--page)}
  .stage{position:relative;width:741px;height:1200px}
  .newsletter{
    position:absolute;left:240px;top:26px;width:520px;height:2296px;
    transform:scale(.5);transform-origin:0 0;
    background:var(--page);box-shadow:0 0 12px rgba(0,0,0,.12);
    font-family:"Open Sans",sans-serif;font-weight:300;color:var(--ink);
  }
  .section{position:absolute;left:0;width:520px}
  .sand{background:var(--sand)}
  .abs{position:absolute}
  .photo{position:absolute}
  .headline{font-family:"Yanone Kaffeesatz",sans-serif;font-weight:300;color:var(--accent);line-height:1.05}
  .body{font-size:12px;line-height:17.6px;letter-spacing:-.2px}
  .btn{position:absolute;background:var(--accent);color:#fff;font-weight:600;text-align:center;
       font-size:10.5px;letter-spacing:.2px;text-transform:uppercase}
  .brand{position:absolute;left:0;width:520px;top:35px;text-align:center}
  .brand-dot{display:block;width:34px;height:34px;margin:0 auto 10px;border-radius:50%;border:2px solid #e9a25a}
  .brand-name{font-family:"Open Sans",sans-serif;font-weight:300;font-size:22px;letter-spacing:1px;color:var(--muted)}
  .kicker{font-family:"Kaushan Script",cursive;color:#fff;font-size:24px;text-align:center;width:520px;left:0}
  .card{position:absolute;top:615px;width:195px;height:240px;background:var(--card)}
  .card .photo{left:0;top:0;width:195px;height:95px}
  .card h3{position:absolute;top:98px;width:195px;text-align:center;font-size:27px}
  .card p{position:absolute;top:156px;left:8px;width:179px;text-align:center}
  .tile{position:absolute;top:0;width:102px;height:213px}
  .tile .photo{left:0;top:0;width:102px;height:165px}
  .tile span{position:absolute;left:0;top:165px;width:102px;height:48px;padding:16px 0 0 8px;
       font-family:"Yanone Kaffeesatz",sans-serif;font-size:11px;line-height:11px;color:#fff;text-transform:uppercase}
  .social{position:absolute;top:2168px;width:30px;height:30px;border-radius:50%;background:#d9d5d1}
  .footer{position:absolute;left:0;width:520px;text-align:center;font-size:8.5px;line-height:10px}
  .footer a{color:var(--accent);font-weight:700;text-decoration:underline}
</style>
</head>
<body>
<div class="stage">
  <main class="newsletter">

    <section class="section sand" style="top:0;height:480px">
      <div class="brand"><span class="brand-dot"></span><span class="brand-name">Atemkreis Nord</span></div>
      <svg class="abs" style="left:72px;top:136px" width="380" height="225" viewBox="0 0 380 225">
        <rect x="36" y="1" width="308" height="204" rx="5" fill="#e2e4e6" stroke="#c9cbcd"/>
        <rect x="0" y="205" width="380" height="7" rx="3" fill="#cfd1d3"/>
        <ellipse cx="190" cy="218" rx="180" ry="3" fill="#d8cfc6"/>
      </svg>
      <div class="photo" role="img" aria-label="Frau meditiert im Lotussitz auf einer Yogamatte in einem hellen Wohnzimmer"
           style="left:114px;top:148px;width:296px;height:186px;background:linear-gradient(120deg,#c9c2b6,#f2eee6 55%,#aab0b6)"></div>
      <div class="abs kicker" style="top:368px">Entdecke jetzt</div>
      <div class="abs headline" style="left:0;width:520px;top:398px;text-align:center;font-size:48px">Online Privatyoga</div>
    </section>
    <div class="btn" style="left:171px;top:462px;width:180px;height:30px;line-height:30px;font-size:14px;text-transform:none">Jetzt mehr erfahren</div>

    <p class="abs body" style="left:80px;top:516px;width:360px;text-align:center">Privatyoga bietet dir – Eins zu Eins Übungen. Ich zeige dir in Privatstunden wie du bestmöglichst, nicht durch Symptombe­handlung, sondern durch Mensch in deiner Ganzheit zu besse­rem Umgang und Wohlbefinden zurückfindest …</p>

    <article class="card" style="left:57px">
      <div class="photo" role="img" aria-label="Hand massiert eine Schulter" style="background:linear-gradient(135deg,#e9ddd2,#c9b3a3)"></div>
      <h3 class="headline">Mehr über<br>Online Privatyoga</h3>
      <p class="body">Du lernst Techniken, die du selbstständig anwenden und für dich umsetzen kannst.</p>
    </article>
    <div class="btn" style="left:86px;top:842px;width:138px;height:28px;line-height:28px">Mehr erfahren</div>

    <article class="card" style="left:270px">
      <div class="photo" role="img" aria-label="Frau übt den Unterarmstütz vor einem Laptop" style="background:linear-gradient(135deg,#d8cab9,#8f8274)"></div>
      <h3 class="headline">Trainiere wann und<br>wo du willst</h3>
      <p class="body">Du übst und entspannst<br>dich in geschützter Atmo­-<br>sphäre, z.B bei dir zu Hause.</p>
    </article>
    <div class="btn" style="left:297px;top:842px;width:138px;height:28px;line-height:28px">Stunden buchen</div>

    <section class="section sand" style="top:930px;height:288px">
      <div class="photo" role="img" aria-label="Älteres Paar macht zu Hause gemeinsam Kniebeugen" style="left:0;top:32px;width:195px;height:220px;background:linear-gradient(135deg,#cfd3cf,#b9a594 60%,#8e8f8a)"></div>
      <h2 class="abs headline" style="left:252px;top:30px;font-size:29px">Yoga fördert<br>die Gelassenheit</h2>
      <p class="abs body" style="left:252px;top:90px;width:205px">Yoga für ein entspannteres Leben …<br>mit Gesundheit und Fitness. Jeder<br>weiß, Bewegung in den Alltag einzu-<br>bauen ist enorm wichtig für unsere<br>Gesundheit. Und diese noch zu er-<br>gänzen mit der Entspannung der<br>pure Luxus.</p>
      <div class="btn" style="left:253px;top:225px;width:154px;height:28px;line-height:28px">Mehr erfahren</div>
    </section>

    <section class="section" style="top:1218px;height:315px">
      <h2 class="abs headline" style="left:50px;width:220px;top:45px;text-align:right;font-size:29px">YOGA ist für jeden</h2>
      <p class="abs body" style="left:50px;width:220px;top:82px;text-align:right">Du musst weder sportlich oder ge-<br>lenkig sein, auch das Alter spielt keine<br>Rolle. Jeder kann jederzeit mit der<br>Praxis des Yoga beginnen. Es ist auch<br>nicht wichtig die Positionen möglichst<br>perfekt einnehmen zu können, denn<br>jeder Körper ist einzigartig.</p>
      <div class="btn" style="left:135px;top:216px;width:136px;height:28px;line-height:28px">Jetzt buchen</div>
      <div class="photo" role="img" aria-label="Mutter und Kind üben gemeinsam den herabschauenden Hund" style="left:323px;top:37px;width:197px;height:222px;background:linear-gradient(135deg,#e6e3dc,#c6bdb1 60%,#7c7f86)"></div>
    </section>

    <section class="section sand" style="top:1533px;height:252px">
      <h2 class="abs headline" style="left:0;width:520px;top:32px;text-align:center;font-size:29px">Weitere Kurs Angebote</h2>
    </section>
    <div class="abs" style="left:57px;top:1620px;width:408px;height:213px">
      <div class="tile" style="left:0"><div class="photo" role="img" aria-label="Mann meditiert mit gefalteten Händen" style="background:linear-gradient(#c9b6a6,#7a4a3a)"></div><span style="background:var(--adult)">Yoga für<br>Erwachsene</span></div>
      <div class="tile" style="left:102px"><div class="photo" role="img" aria-label="Mädchen sitzt im Lotussitz" style="background:linear-gradient(#efeae5,#b9b1c6)"></div><span style="background:var(--kids)">Yoga für<br>Kinder</span></div>
      <div class="tile" style="left:204px"><div class="photo" role="img" aria-label="Babybauch einer schwangeren Frau" style="background:linear-gradient(90deg,#f3efea,#d8b9a3)"></div><span style="background:var(--mama)">Yoga für<br>Schwangere</span></div>
      <div class="tile" style="left:306px"><div class="photo" role="img" aria-label="Ältere Frau meditiert" style="background:linear-gradient(#b8c3c4,#4c7a93)"></div><span style="background:var(--senior)">Yoga für<br>Senioren</span></div>
    </div>

    <section class="section sand" style="top:1925px;height:207px">
      <h2 class="abs headline" style="left:0;width:520px;top:66px;text-align:center;font-size:29px">Kontaktiere mich und buche<br>deinen Kurs</h2>
      <p class="abs body" style="left:90px;width:340px;top:125px;text-align:center">Ich bin zertifizierte Yogalehrerin und habe mich zusätzlich für Yogatherapie und Yoga für Kinder weitergebildet. Seit über elf Jahren praktiziere ich hauptsächlich Hatha Yoga.</p>
      <div class="abs" style="left:0;width:520px;top:182px;text-align:center;font-family:'Kaushan Script',cursive;font-size:26px;color:var(--accent)">Marlene Voss</div>
    </section>
    <div class="photo" role="img" aria-label="Porträt der Yogalehrerin" style="left:208px;top:1873px;width:104px;height:104px;border-radius:50%;background:radial-gradient(circle,#e9cdb6,#f3eee8)"></div>

    <span class="social" style="left:224px"></span>
    <span class="social" style="left:262px"></span>
    <p class="footer" style="top:2212px">www.atemkreis-nord.ch</p>
    <p class="footer" style="top:2228px">Lorem ipsum dolor sit amet, consectetuer adipiscing elit aenean: <a>Unsubscribe here</a><br>commodo ligula eget dolor. Aenean massa. Cum sociis natoque penatibus et ma</p>

  </main>
</div>
</body>
</html>
```